Seven nights at the harbour

Creation of the cover for the book: "Sept nuits sur le quai du port" with the joined photo of a 70 years old lady.
Title: "Seven nights along the old harbour"
Author: "Mireille Vaston"
Publisher: "Editions Morvane" (should be at the bottom of the page)
Format: 14 x 20.5 cm
The story: A senior lady (70 years old), divorced, with a beautiful face, still wants to seduce, even young men.
We found the perfect photo for the woman. We would like to ask you to make a modern cover from it.
Besoin de quelques jours pour choisir un design
Target Market(s)
Novels reader (adults)
Industry/Entity Type
book

```html
<!DOCTYPE html>
<html lang="fr">
<head>
<meta charset="utf-8">
<title>Sept nuits sur le quai du port — Mireille Vaston</title>
<link rel="stylesheet" href="https://fonts.googleapis.com/css2?family=Quicksand:wght@400;500;700&display=swap">
<style>
  :root {
    --cover-bg: #27282a;
    --title-white: #ffffff;
    --author-pink: #d44ec0;
    --hair-light: #f2f3f3;
    --hair-mid: #b9bdc0;
    --hair-dark: #6e7478;
  }
  html, body {
    margin: 0;
    padding: 0;
    width: 840px;
    height: 1200px;
    overflow: hidden;
    background: var(--cover-bg);
  }
  .cover {
    position: relative;
    width: 840px;
    height: 1200px;
    background: var(--cover-bg);
    font-family: "Quicksand", sans-serif;
  }
  .cover-title-art {
    position: absolute;
    left: 0;
    top: 0;
    width: 840px;
    height: 720px;
  }
  .title-word {
    font-family: "Quicksand", sans-serif;
    font-weight: 700;
  }
  .subtitle {
    position: absolute;
    left: 0;
    top: 736px;
    width: 840px;
    margin: 0;
    text-align: center;
    color: var(--title-white);
    font-weight: 700;
    font-size: 64px;
    line-height: 80px;
    letter-spacing: 1px;
  }
  .author {
    position: absolute;
    left: 0;
    top: 1058px;
    width: 840px;
    margin: 0;
    text-align: center;
    color: var(--author-pink);
    font-weight: 500;
    font-size: 52px;
    line-height: 60px;
    letter-spacing: 7px;
  }
  .publisher {
    position: absolute;
    left: 0;
    top: 1126px;
    width: 840px;
    margin: 0;
    text-align: center;
    color: var(--title-white);
    font-weight: 400;
    font-size: 30px;
    line-height: 40px;
  }
</style>
</head>
<body>
<main class="cover">
  <svg class="cover-title-art" viewBox="0 0 840 720" role="img" aria-label="Titre Sept nuits rempli par la photo d'une femme de 70 ans aux cheveux blancs et gris">
    <defs>
      <linearGradient id="hair-fill" gradientUnits="userSpaceOnUse" x1="20" y1="130" x2="820" y2="710">
        <stop offset="0" stop-color="var(--hair-mid)" style="stop-color: var(--hair-mid)"/>
        <stop offset="0.3" stop-color="var(--hair-light)" style="stop-color: var(--hair-light)"/>
        <stop offset="0.55" stop-color="var(--hair-dark)" style="stop-color: var(--hair-dark)"/>
        <stop offset="0.8" stop-color="var(--hair-light)" style="stop-color: var(--hair-light)"/>
        <stop offset="1" stop-color="var(--hair-mid)" style="stop-color: var(--hair-mid)"/>
      </linearGradient>
    </defs>
    <text class="title-word" x="20" y="448" font-size="440" textLength="805" lengthAdjust="spacingAndGlyphs" fill="url(#hair-fill)">SEPT</text>
    <text class="title-word" x="20" y="704" font-size="350" textLength="805" lengthAdjust="spacingAndGlyphs" fill="url(#hair-fill)">NUITS</text>
  </svg>
  <h2 class="subtitle">SUR LE QUAI DU PORT</h2>
  <p class="author">MIREILLE VASTON</p>
  <p class="publisher">Editions Morvane</p>
</main>
</body>
</html>
```